Business card for Luxury Portable Restroom Trailer company

We are a Luxury Portable Restroom Trailer Company Called PELIKAR HIRES. Based in Orange County California. We provide portable restroom trailers for events, such as, Weddings, Concerts, Charity events, Sporting events, Tournaments, Corporate events, ect. We rent and Sell the Luxury restrooms. Our colors are white, grey, and Orange. As you will see in the logo we uploaded.
There are 2 people in the company so the names and titles will change for the 3 people but card will remain the same. Here is the information for each Person: Dennis Moyle CFO 555 018-3647
next Person: Wesley Tanford VP 555 018-3647
Next Person: Miles Tanford CEO 555 018-3647
Information to include on the card: Luxury Restroom Trailers Rental and Sales. Weddings, Concerts, Charity, Sporting and Corp. Events.

```html
<!DOCTYPE html>
<html lang="en">
<head>
<meta charset="utf-8">
<title>Pelikar Hires — Business Card</title>
<link rel="stylesheet" href="https://fonts.googleapis.com/css2?family=Barlow:wght@300;400;600;700&display=swap">
<style>
  :root {
    --canvas: #c9c9cb;
    --card-white: #fbfbfb;
    --card-dark: #434347;
    --card-dark-mark: #4b4b50;
    --ink: #3a3a3e;
    --ink-soft: #5a5a5e;
    --orange: #ec5a1f;
    --white: #ffffff;
  }
  * { margin: 0; padding: 0; box-sizing: border-box; }
  html, body {
    width: 1200px; height: 1200px; overflow: hidden;
    background: var(--canvas);
    font-family: "Barlow", sans-serif;
  }
  .sheet {
    width: 1200px; height: 1200px;
    display: flex; flex-direction: column;
    align-items: center; justify-content: center; gap: 60px;
  }
  .card {
    position: relative;
    width: 700px; height: 400px;
    overflow: hidden;
    box-shadow: 0 10px 30px rgba(0,0,0,0.12);
  }

  /* Front */
  .card--front { background: var(--card-white); color: var(--ink); }
  .person {
    position: absolute; left: 70px; top: 62px;
  }
  .person__name {
    font-size: 22px; font-weight: 300; letter-spacing: 1px;
    text-transform: uppercase; color: var(--ink);
  }
  .person__surname { font-weight: 700; }
  .person__divider { font-weight: 300; color: var(--ink-soft); margin: 0 6px; }
  .person__phone {
    margin-top: 4px;
    font-size: 46px; font-weight: 300; letter-spacing: 1px;
    color: var(--orange);
  }
  .brand {
    position: absolute;
    display: flex; align-items: center; gap: 10px;
    font-weight: 700; text-transform: uppercase; letter-spacing: 1px;
    white-space: nowrap;
  }
  .brand__square { display: block; flex: none; }
  .card--front .brand {
    right: 56px; top: 176px;
    font-size: 24px; color: var(--ink);
  }
  .card--front .brand__square { width: 16px; height: 16px; background: var(--orange); }
  .tagline {
    position: absolute; right: 56px; bottom: 56px;
    width: 250px;
    font-size: 13px; line-height: 1.45; font-weight: 400;
    text-transform: uppercase; letter-spacing: 0.3px;
    color: var(--ink-soft);
  }

  /* Back */
  .card--back { background: var(--card-dark); }
  .card--back .emblem {
    position: absolute; left: 60px; top: 170px;
    width: 380px; height: 380px; border-radius: 50%;
    background: var(--card-dark-mark);
  }
  .card--back .brand {
    right: 50px; top: 120px;
    font-size: 40px; color: var(--white);
  }
  .card--back .brand__square { width: 24px; height: 24px; background: var(--orange); }
</style>
</head>
<body>
<main class="sheet">
  <section class="card card--front" aria-label="Business card front">
    <div class="person">
      <p class="person__name">Miles <span class="person__surname">Tanford</span><span class="person__divider">|</span>CEO</p>
      <p class="person__phone">555 018-3647</p>
    </div>
    <div class="brand"><span class="brand__square"></span>Pelikar Hires</div>
    <p class="tagline">Luxury restroom trailers rental and sales. Weddings, concerts, charity, sporting and corp. events.</p>
  </section>

  <section class="card card--back" aria-label="Business card back">
    <div class="emblem" role="img" aria-label="Faint large brand emblem illustration"></div>
    <div class="brand"><span class="brand__square"></span>Pelikar Hires</div>
  </section>
</main>
</body>
</html>
```